Kelvo-Dex Flyer (Business Launch)

Using my existing log design for Kelvo-Dex Mobile Mechanics, I would like a flyer designed. This would be used for advertising, letterbox drops, handing to the public , door knocking ect.

I'm looking for clean cut simple though with the wow factor, I was thinking of even having the flyer in the shape of a van to promote that I'm a mobile business (I come to you ect)

I've attached copies of my logo and business cards.

I would like the following list of services we provide listed on the flyer (see back of business card).
7 day service (we come to you)
10% discount for online/email booking-enquiry

I think this should be enough for now.

I'm launching this business to aiming to hit the ground running,

Target Market(s)

All motor vehicle owners, house holds, businesses

Industry/Entity Type

Automotive

Font styles to use
Sans Serif
Other font styles liked:
• refer images

Colors
0355a3

Requirements
Must have
• services offered, logo, 7 days, we come to or or catchy phrase to let people know this.
• 10% discount for online/email booking enquiries
• Maintenance Package Servicing from $149 conditions apply
• my preference is for blue, grey and while colour scheme, though also happy to accept artistic design ideas to these.
Nice to have
• Wow factor, brochure that stand out from the rest
• Different share brochure in shape of work van (refer varsona kribo van)
Should not have
• Not looking for a cheap quick fix, I'm wanting to create a brand .

```html
<!DOCTYPE html>
<html lang="en">
<head>
<meta charset="utf-8">
<title>Kelvo-Dex Mobile Mechanics Flyer</title>
<link href="https://fonts.googleapis.com/css2?family=Anton&family=Ubuntu:wght@500;700&family=Open+Sans:wght@400;600&display=swap" rel="stylesheet">
<style>
  :root {
    --blue: #4586c9;
    --blue-deep: #0355a3;
    --charcoal: #3a3b3d;
    --grey: #7c7d80;
    --dark: #1b1b1c;
    --white: #ffffff;
    --stage: #2b2b2c;
  }
  html, body {
    margin: 0;
    width: 1200px;
    height: 1200px;
    overflow: hidden;
    background: var(--stage);
  }
  .flyer {
    position: absolute;
    left: 315px;
    top: 30px;
    width: 600px;
    height: 1200px;
    transform: scale(0.95);
    transform-origin: top left;
    background: var(--white);
    overflow: hidden;
    box-shadow: 0 10px 30px rgba(0,0,0,.5);
  }
  .flyer-shapes { position: absolute; inset: 0; }
  .brand {
    position: absolute;
    left: 122px;
    top: 48px;
    display: flex;
    align-items: center;
    gap: 16px;
  }
  .brand-dot {
    width: 74px; height: 74px;
    border-radius: 50%;
    background: var(--blue);
  }
  .brand-name {
    font-family: "Ubuntu", sans-serif;
    font-weight: 700;
    font-size: 50px;
    line-height: 1;
    color: var(--charcoal);
  }
  .brand-tagline {
    font-family: "Ubuntu", sans-serif;
    font-weight: 700;
    font-size: 20px;
    letter-spacing: 1px;
    color: var(--grey);
    margin-top: 4px;
  }
  .headline, .service {
    font-family: "Anton", sans-serif;
    color: var(--white);
    text-shadow: 2px 3px 4px rgba(0,0,0,.6);
    margin: 0;
    font-weight: 400;
  }
  .headline {
    position: absolute;
    left: 40px;
    top: 312px;
    font-size: 52px;
    line-height: 64px;
  }
  .services {
    position: absolute;
    right: 42px;
    top: 500px;
    text-align: right;
    list-style: none;
    margin: 0; padding: 0;
  }
  .service { font-size: 38px; line-height: 42px; margin-bottom: 30px; }
  .service:first-child { margin-bottom: 30px; }
  .footer {
    position: absolute;
    left: 30px;
    right: 30px;
    top: 1078px;
    font-family: "Open Sans", sans-serif;
    color: var(--charcoal);
  }
  .abn { font-size: 14px; font-weight: 600; padding-bottom: 4px; border-bottom: 1.5px solid var(--blue); }
  .contacts {
    display: grid;
    grid-template-columns: 180px 1fr;
    row-gap: 12px;
    margin-top: 12px;
    font-size: 21px;
  }
  .contact { display: flex; align-items: center; gap: 8px; }
  .contact svg { width: 22px; height: 22px; flex: none; }
  .base-band { position: absolute; left: 0; right: 0; bottom: 0; height: 18px; background: var(--blue); }
</style>
</head>
<body>
<main class="flyer">
  <svg class="flyer-shapes" viewBox="0 0 600 1200" width="600" height="1200">
    <defs>
      <radialGradient id="photoTone" cx="0.4" cy="0.55" r="0.7">
        <stop offset="0" stop-color="#5c5d5f"/>
        <stop offset="0.55" stop-color="#2e2f30"/>
        <stop offset="1" stop-color="#121213"/>
      </radialGradient>
    </defs>
    <polygon points="295,245 600,65 600,420" fill="var(--blue)"/>
    <polygon points="0,725 0,1060 290,888" fill="var(--blue)"/>
    <g role="img" aria-label="Black and white close-up photograph of a six-speed manual gear stick knob">
      <polygon points="0,80 600,420 600,1080 0,725" fill="url(#photoTone)"/>
    </g>
  </svg>

  <div class="brand">
    <div class="brand-dot"></div>
    <div>
      <div class="brand-name">Kelvo-Dex</div>
      <div class="brand-tagline">MOBILE MECHANICS</div>
    </div>
  </div>

  <h1 class="headline">Mobile Service<br>7 days a Week</h1>

  <ul class="services">
    <li class="service">10% discount for online/<br>email booking-enquiry</li>
    <li class="service">Servicing &amp; Repairs</li>
    <li class="service">Manufacturers Log<br>Book Service</li>
    <li class="service">Pre-Purchase<br>Inspections</li>
  </ul>

  <footer class="footer">
    <div class="abn">ABN 41 555 000 918</div>
    <div class="contacts">
      <div class="contact">
        <svg viewBox="0 0 22 22"><circle cx="11" cy="11" r="11" fill="var(--blue)"/><path d="M6 9c0-2 2-3 5-3s5 1 5 3l-2 1-1-2h-4l-1 2zM7 11h8l1 5H6z" fill="#fff"/></svg>
        <span>1300 555 014</span>
      </div>
      <div class="contact">
        <svg viewBox="0 0 22 22"><circle cx="11" cy="11" r="11" fill="var(--blue)"/><circle cx="11" cy="11" r="5.5" fill="none" stroke="#fff" stroke-width="1.5"/><path d="M5.5 11h11M11 5.5c-3 3-3 8 0 11M11 5.5c3 3 3 8 0 11" fill="none" stroke="#fff" stroke-width="1.2"/></svg>
        <span>www.kelvo-dex.com.au</span>
      </div>
      <div class="contact">
        <svg viewBox="0 0 22 22"><circle cx="11" cy="11" r="11" fill="var(--blue)"/><rect x="7.5" y="5" width="7" height="12" rx="1.5" fill="#fff"/><rect x="8.7" y="6.5" width="4.6" height="7" fill="var(--blue)"/></svg>
        <span>0400 555 273</span>
      </div>
      <div class="contact">
        <svg viewBox="0 0 22 22"><circle cx="11" cy="11" r="11" fill="var(--blue)"/><rect x="5.5" y="7" width="11" height="8" rx="1" fill="#fff"/><path d="M5.5 7.5l5.5 4 5.5-4" fill="none" stroke="var(--blue)" stroke-width="1.2"/></svg>
        <span>admin@kelvo-dex.com.au</span>
      </div>
    </div>
  </footer>

  <div class="base-band"></div>
</main>
</body>
</html>
```